The Lone Staple Plan: Reshape Your Bond with Meals in Only 30 Days

I want a book cover for a paperback non-fiction book 30 day challenge to transform you relationship with your food, diet and lifestyle for longterm health and vitality. I would like to incorporate two photos on the front cover, one of a Greek salad and one of me the author. I have uploaded the four photos. Use which of each pair you think best. Because of my name, I want the photo on the cover. Otherwise folks assume Marla is a guy.
I am looking at best selling health books and they seem to be on the lighter side color-wise, with horizontal design. Green and orange seem to work most often, though my logo is a bluish turquoise (https://marlaquenby.com). I would imagine a light background, clear simple fonts. Looking forward to your designs!

Target Market(s)

Women around 35-40 confused by conflicting nutrition information but dedicated to better health haelthy

Industry/Entity Type

nutrition and wellness

Font styles to use
Serif

Colors
00AB8E
00BBA5
67D7C9
C6EFE9
E9F9F6
F0912C
F2A743
F7CA91
FBE8D2
FDF5EE
EE7325
F08F49
F5BC92
FAE3D3
FDF4ED

Requirements
Must have
• Clear simple look with room for an endorsement
Nice to have
• Hints of natural scenes and happy places
Should not have
• Dark or ominous feel

```html
<!DOCTYPE html>
<html lang="en">
<head>
<meta charset="utf-8">
<title>The Lone Staple Plan – Book Cover Wrap</title>
<link rel="stylesheet" href="https://fonts.googleapis.com/css2?family=Playfair+Display:wght@400;700&family=Oswald:wght@500;600&family=Montserrat:wght@500&family=Space+Mono&family=Great+Vibes&display=swap">
<style>
  :root {
    --page-bg: #e4e4e4;
    --green-light: #33b24d;
    --green-dark: #06693a;
    --green-title: #15783f;
    --green-accent: #3aa94a;
    --body-text: #16713d;
    --imprint: #2aa6c0;
    --white: #ffffff;
    --paper: #f7f7f5;
  }
  * { margin: 0; padding: 0; box-sizing: border-box; }
  html, body { width: 1200px; height: 857px; overflow: hidden; background: var(--page-bg); }
  .canvas { position: relative; width: 1200px; height: 857px; }

  .panel { position: absolute; top: 118px; height: 617px; overflow: hidden; }
  .green-fill { background: linear-gradient(160deg, var(--green-light), var(--green-dark)); }

  .small-copy {
    font: 500 6.6px/9.4px "Montserrat", sans-serif;
    letter-spacing: 0.3px; text-align: justify; hyphens: auto;
  }

  /* Back cover */
  .back-cover { left: 89px; width: 421px; background: var(--paper); }
  .author-column { position: absolute; left: 0; top: 0; width: 187px; height: 100%; }
  .author-photo {
    position: absolute; left: 16px; top: 7px; width: 142px; height: 192px;
    border: 6px solid var(--white);
    background: linear-gradient(180deg, #f2f2f0 0%, #d9d2c2 60%, #cdb98a 100%);
  }
  .author-name {
    position: absolute; left: 15px; top: 204px; width: 145px; white-space: nowrap;
    font: 400 18.5px/1 "Playfair Display", serif; color: var(--white); letter-spacing: 1.2px;
  }
  .author-bio {
    position: absolute; left: 15px; top: 236px; width: 143px; height: 338px; overflow: hidden;
    color: var(--white);
  }
  .blurb-column { position: absolute; left: 187px; top: 0; width: 207px; height: 100%; background: var(--white); }
  .blurb-title {
    margin-top: 20px; text-align: center;
    font: 700 20px/24px "Playfair Display", serif; color: var(--green-title);
  }
  .blurb-subtitle {
    text-align: center; margin-top: 0;
    font: 500 8.2px/1 "Oswald", sans-serif; color: var(--green-accent); letter-spacing: -0.1px;
  }
  .blurb-text {
    position: absolute; left: 14px; top: 94px; width: 181px; height: 385px; overflow: hidden;
    color: var(--body-text);
  }
  .imprint {
    position: absolute; left: 0; width: 100%; top: 562px; text-align: center;
    font: 700 11px/1 "Playfair Display", serif; color: var(--imprint);
  }
  .back-edge { position: absolute; left: 394px; top: 0; width: 27px; height: 100%; }

  /* Spine */
  .spine { left: 563px; width: 69px; }
  .spine-text { position: absolute; writing-mode: vertical-rl; color: var(--white); white-space: nowrap; }
  .spine-title { left: 27px; top: 88px; font: 700 25px/1 "Playfair Display", serif; }
  .spine-subtitle { left: 11px; top: 124px; font: 400 9.4px/1 "Space Mono", monospace; letter-spacing: 2.2px; }
  .spine-by { position: absolute; top: 576px; width: 100%; text-align: center; font: 400 13px/1 "Great Vibes", cursive; color: var(--white); }
  .spine-author { position: absolute; top: 596px; width: 100%; text-align: center; font: 400 8.2px/1 "Playfair Display", serif; color: var(--white); }

  /* Front cover */
  .front-cover { left: 677px; width: 421px; background: var(--white); }
  .front-band { position: absolute; left: 0; top: 0; width: 100%; height: 32px; }
  .front-title {
    position: absolute; top: 55px; width: 100%; text-align: center;
    font: 700 45px/49px "Playfair Display", serif; color: var(--green-title);
  }
  .front-subtitle {
    position: absolute; top: 162px; width: 100%; text-align: center; white-space: nowrap;
    font: 600 20px/1 "Oswald", sans-serif; color: var(--green-accent); letter-spacing: -0.4px;
  }
  .salad-photo {
    position: absolute; left: 0; top: 305px; width: 100%; height: 312px;
    background: radial-gradient(ellipse at 35% 70%, #5cae57 0%, #3c9a46 40%, #237f3c 100%);
  }
  .portrait {
    position: absolute; left: 222px; top: 212px; width: 192px; height: 192px; border-radius: 50%;
    border: 4px solid var(--white);
    background: linear-gradient(180deg, #fafafa 0%, #ece6da 55%, #d7c390 100%);
  }
  .front-by { position: absolute; left: 110px; top: 548px; font: 400 34px/1 "Great Vibes", cursive; color: var(--white); }
  .front-author { position: absolute; left: 135px; top: 580px; font: 400 22px/1 "Playfair Display", serif; color: var(--white); letter-spacing: 0.5px; }
</style>
</head>
<body>
<main class="canvas">

  <section class="panel back-cover" aria-label="Back cover">
    <div class="author-column green-fill">
      <div class="author-photo" role="img" aria-label="Portrait photo of author Marla Quenby"></div>
      <h2 class="author-name">MARLA QUENBY</h2>
      <p class="author-bio small-copy">Marla Quenby is an internationally known author, speaker, counselor, and media personality. Known especially for her sound advice on parenting and healthy lifestyle, she delights in bringing out the best in people, for their relationships, health, and spiritual being. She has a uniquely diverse set of accomplishments, first and foremost as wife, mother, grandmother, and daughter, and then as family therapist, nutrition educator, lawyer, theologian, world traveler, and mentor to home-based entrepreneurs. Because of this diverse background and her passion for making the world a better place, she has a rare ability to cut through the noise in a person’s life and help her students, clients, customers, and team members to discover their true power and find their path to becoming their best self.sum dolor sit amet, cons ectetuer adipiscing elit, sed diam nonummy nibh euismod tincidunt ut laoreet dolore magna aliquam erat volutpat. Ut wisi enim ad minim veniam, quis nostrud exerci tation ullamcorper suscipit lobortis nisl ut aliquip ex ea commodo consequat. Lorem ipsum dolor sit amet, con-</p>
    </div>

    <div class="blurb-column">
      <h2 class="blurb-title">THE LONE<br>STAPLE PLAN</h2>
      <p class="blurb-subtitle">RESHAPE YOUR BOND WITH MEALS IN ONLY 30 DAYS</p>
      <div class="blurb-text small-copy">
        <p>Lorem ipsum dolor sit amet, consectetuer adipiscing elit, sed diam nonummy nibh euismod tincidunt ut laoreet dolore magna aliquam erat volutpat. Ut wisi enim ad minim veniam, quis nostrud exerci tation ullamcorper suscipit lobortis nisl ut aliquip ex ea commodo consequat. Duis autem vel eum iriure dolor in hendrerit in vulputate velit esse molestie consequat, vel illum dolore eu feugiat nulla facilisis at vero eros et accumsan et iusto odio dignissim qui blandit praesent luptatum zzril delenit augue duis dolore te feugait nulla facilisi.</p>
        <p>Lorem ipsum dolor sit amet, cons ectetuer adipiscing elit, sed diam nonummy nibh euismod tincidunt ut laoreet dolore magna aliquam erat volutpat. Ut wisi enim ad minim veniam, quis nostrud exerci tation ullamcorper suscipit lobortis nisl ut aliquip ex ea commodo consequat.</p>
        <p>Lorem ipsum dolor sit amet, consectetuer adipiscing elit, sed diam nonummy nibh euismod tincidunt ut laoreet dolore magna aliquam erat volutpat. Ut wisi enim ad minim veniam, quis nostrud exerci tation ullamcorper suscipit lobortis nisl ut aliquip ex ea commodo consequat. Duis autem vel eum iriure dolor in hendrerit in vulputate velit esse molestie consequat, vel illum dolore eu feugiat nulla facilisis at vero eros et accumsan et iusto odio dignissim qui blandit praesent luptatum zzril delenit augue duis dolore te feugait nulla facilisi.</p>
        <p>Lorem ipsum dolor sit amet, cons ectetuer adipiscing elit, sed diam nonummy nibh euismod tincidunt ut laoreet dolore magna aliquam erat volutpat. Ut wisi enim ad minim veniam, quis nostrud exerci tation ullamcorper suscipit lobor-</p>
      </div>
      <p class="imprint">Quenby Wellness</p>
    </div>

    <div class="back-edge green-fill"></div>
  </section>

  <section class="panel spine green-fill" aria-label="Spine">
    <h2 class="spine-text spine-title">THE LONE STAPLE PLAN</h2>
    <p class="spine-text spine-subtitle">RESHAPE YOUR BOND WITH MEALS IN ONLY 30 DAYS</p>
    <p class="spine-by">by</p>
    <p class="spine-author">MARLA QUENBY</p>
  </section>

  <section class="panel front-cover" aria-label="Front cover">
    <div class="front-band green-fill"></div>
    <h1 class="front-title">THE LONE<br>STAPLE PLAN</h1>
    <p class="front-subtitle">RESHAPE YOUR BOND WITH MEALS IN ONLY 30 DAYS</p>
    <div class="salad-photo" role="img" aria-label="Green-tinted photo of a Greek salad in a bowl with serving spoons and bottles of olive oil and vinegar"></div>
    <div class="portrait" role="img" aria-label="Circular portrait photo of author Marla Quenby"></div>
    <p class="front-by">by</p>
    <p class="front-author">MARLA QUENBY</p>
  </section>

</main>
</body>
</html>
```